Residential Construction Business - Site Signage

I need a design made for a site fence banner. We have a logo and branding so the design would need to be aligned with this. It would need to be made to specific size ratio so that it can be sent to the maker for production.
ratio : 4600 wide x 1700 high
The design should feature our website and also the slogan
"don't move, re-imagine"

Target Market(s)

potential clients

Industry/Entity Type

construction

Font styles to use
Other font styles liked:
• to match branding

Colors
0054AA
0677BA
7BADD7
CADEEF
E8F1F8

Requirements
Must have
• www.velmbuild.com.au Majority of the sign is our brand logo
Nice to have
• Majority of the sign is our brand logo
Should not have
• colors and themes that arent brand relevant

```html
<!DOCTYPE html>
<html lang="en">
<head>
<meta charset="utf-8">
<title>Velmbuild – Site Fence Banner</title>
<link rel="stylesheet" href="https://fonts.googleapis.com/css2?family=Poppins:wght@400;600;700&display=swap">
<style>
  :root {
    --backdrop: #5f5f5f;
    --brand-navy: #003d5e;
    --banner-white: #ffffff;
    --url-ink: #0a0a0a;
  }
  html, body {
    margin: 0;
    padding: 0;
    width: 1200px;
    height: 600px;
    overflow: hidden;
    background: var(--backdrop);
  }
  .canvas {
    position: relative;
    width: 1200px;
    height: 600px;
  }
  .fence-banner {
    position: absolute;
    left: 94px;
    top: 109px;
    width: 1008px;
    height: 372px;
    display: block;
  }
  .banner-base { fill: var(--banner-white); }
  .navy-field { fill: var(--brand-navy); }
  .hoist-line { stroke: var(--banner-white); stroke-width: 2.4; }
  .slogan {
    font-family: "Poppins", sans-serif;
    fill: var(--banner-white);
  }
  .slogan-strong { font-weight: 700; font-size: 68px; letter-spacing: -1px; }
  .slogan-light { font-weight: 400; font-size: 72px; letter-spacing: -1px; }
  .brand-name {
    font-family: "Poppins", sans-serif;
    font-weight: 600;
    font-size: 31px;
    fill: var(--brand-navy);
  }
  .site-url {
    font-family: "Poppins", sans-serif;
    font-weight: 600;
    font-size: 46px;
    fill: var(--url-ink);
  }
</style>
</head>
<body>
<main class="canvas">
  <svg class="fence-banner" viewBox="0 0 1008 372" xmlns="http://www.w3.org/2000/svg" aria-label="Velmbuild site fence banner">
    <rect class="banner-base" x="0" y="0" width="1008" height="372"/>
    <polygon class="navy-field" points="0,0 818,0 698,131 818,262 0,262"/>
    <line class="hoist-line" x1="371" y1="0" x2="371" y2="66"/>
    <text class="slogan slogan-strong" x="82" y="125" textLength="414" lengthAdjust="spacingAndGlyphs">don't move,</text>
    <text class="slogan slogan-light" x="82" y="197" textLength="405" lengthAdjust="spacingAndGlyphs">re-imagine</text>
    <text class="brand-name" x="711" y="141" textLength="266" lengthAdjust="spacing">VELMBUILD</text>
    <text class="site-url" x="89" y="322" textLength="831" lengthAdjust="spacing">www.velmbuild.com.au</text>
  </svg>
</main>
</body>
</html>
```